Torvane PT Business Card

I need the card to be bright/bold colours to stand out amongst others.
It needs to have my company logo.
I was not interested in pictures etc just a layout that attracts attention.

I have attached my old design which is very plain. I also needed change the contact details. And my description changed to Personal Trainer
Phone 0427391058
Facebook Torvane PT
No email address please, no street address.
And only Torvane PT (Please remove anything to do with Torvane Supplements)

```html
<!DOCTYPE html>
<html lang="en">
<head>
<meta charset="utf-8">
<title>Torvane PT Business Card</title>
<link rel="stylesheet" href="https://fonts.googleapis.com/css2?family=Cinzel:wght@400;700&family=Pompiere&display=swap">
<style>
  :root {
    --card-white: #ffffff;
    --card-black: #000000;
    --brand-yellow: #dcc61a;
    --brand-yellow-shade: #b7a514;
    --brand-blue: #1e88c1;
    --text-light: #ffffff;
  }
  * { margin: 0; padding: 0; box-sizing: border-box; }
  html, body {
    width: 1200px;
    height: 726px;
    overflow: hidden;
    background: var(--card-white);
  }
  .business-card {
    position: relative;
    width: 1200px;
    height: 726px;
    background: var(--card-white);
    border: 3px solid var(--card-black);
    overflow: hidden;
  }
  .card-shapes {
    position: absolute;
    inset: 0;
  }
  .brand-name {
    position: absolute;
    left: 42px;
    top: 278px;
    width: 510px;
    text-align: center;
    font-family: "Cinzel", serif;
    font-weight: 700;
    font-size: 64px;
    letter-spacing: 1px;
    color: var(--brand-blue);
    line-height: 1;
  }
  .trainer-name {
    position: absolute;
    left: 600px;
    top: 84px;
    width: 580px;
    text-align: center;
    font-family: "Cinzel", serif;
    font-weight: 400;
    font-size: 60px;
    line-height: 1;
    color: var(--text-light);
  }
  .trainer-role {
    position: absolute;
    left: 600px;
    top: 156px;
    width: 580px;
    text-align: center;
    font-family: "Pompiere", sans-serif;
    font-size: 42px;
    line-height: 1;
    color: var(--text-light);
  }
  .contact-line {
    position: absolute;
    font-family: "Pompiere", sans-serif;
    font-size: 40px;
    line-height: 1;
    color: var(--text-light);
  }
  .contact-phone { left: 828px; top: 368px; }
  .contact-social { left: 820px; top: 526px; }
</style>
</head>
<body>
  <div class="business-card">
    <svg class="card-shapes" width="1200" height="726" viewBox="0 0 1200 726" aria-hidden="true">
      <polygon class="dark-panel" points="747,0 1200,0 1200,726 407,726" fill="var(--card-black)"/>
      <polygon class="band-fold" points="589,212 650,212 614,289" fill="var(--brand-yellow-shade)"/>
      <rect class="name-band" x="589" y="71" width="611" height="141" fill="var(--brand-yellow)"/>
      <circle class="icon-circle" cx="751" cy="386" r="50" fill="var(--brand-blue)"/>
      <g class="phone-icon" fill="var(--text-light)">
        <path d="M727 365 c4 -4 9 -4 11 0 l6 10 c2 4 1 7 -2 9 l-4 3 c3 8 9 14 17 17 l3 -4 c2 -3 5 -4 9 -2 l10 6 c4 2 4 7 0 11 l-5 5 c-5 5 -14 4 -24 -2 c-12 -8 -22 -18 -28 -30 c-5 -10 -5 -18 0 -22 z"/>
      </g>
      <g class="signal-waves" fill="none" stroke="var(--text-light)" stroke-width="3" stroke-linecap="round">
        <path d="M758 371 a9 9 0 0 1 9 9"/>
        <path d="M759 362 a18 18 0 0 1 17 17"/>
        <path d="M760 353 a27 27 0 0 1 25 25"/>
      </g>
      <circle class="icon-circle" cx="749" cy="545" r="50" fill="var(--brand-blue)"/>
    </svg>

    <div class="brand-name">TORVANE PT</div>

    <div class="trainer-name">JAMIE KELLAR</div>
    <div class="trainer-role">Personal Trainer</div>

    <div class="contact-line contact-phone">0427391058</div>
    <div class="contact-line contact-social">Torvane PT</div>
  </div>
</body>
</html>
```